Looking for a professional, clean and crisp business card

I am in the underground utilities industry and am just looking for a really impressive business card. I would like our card to be white with our symbol crisp and clear with it protruding. I also have a business partner that will require his name and info on the card once the design is set. I would like to have our website info on the card which is;
http://harbortrenchco.example/

Contact Information for Business Card

Website, contact name, number and email

```html
<!DOCTYPE html>
<html lang="en">
<head>
<meta charset="utf-8">
<title>Harbor Trench Co — Business Card</title>
<link href="https://fonts.googleapis.com/css2?family=Arimo:wght@400;700&display=swap" rel="stylesheet">
<style>
  :root {
    --bg: #2a2a2a;
    --card-dark: #231f20;
    --card-light: #ffffff;
    --ink: #1a1a1a;
    --accent: #2f5aa8;
    --divider: #9a9a9a;
  }
  * { margin: 0; padding: 0; box-sizing: border-box; }
  html, body { width: 1200px; height: 1040px; overflow: hidden; }
  body {
    background: var(--bg);
    font-family: "Arimo", Arial, sans-serif;
    position: relative;
  }
  .card {
    position: absolute;
    left: 250px;
    width: 700px;
    height: 400px;
    box-shadow: 0 12px 30px rgba(0,0,0,0.45);
  }
  .card--back {
    top: 90px;
    background: var(--card-dark);
    border-radius: 90px 0 90px 0;
    display: flex;
    align-items: center;
    justify-content: center;
  }
  .card--front {
    top: 550px;
    background: var(--card-light);
    border-radius: 0 90px 0 90px;
    display: flex;
    align-items: center;
    padding-right: 40px;
  }
  .brand {
    display: flex;
    align-items: center;
    gap: 12px;
    font-weight: 700;
    letter-spacing: 0.3px;
    white-space: nowrap;
  }
  .brand__dot {
    width: 20px;
    height: 20px;
    border-radius: 50%;
    background: var(--accent);
    flex: none;
  }
  .card--back .brand { color: #ffffff; font-size: 34px; }
  .card--front .brand { color: var(--ink); font-size: 25px; }
  .front__brand-area {
    width: 300px;
    flex: none;
    display: flex;
    justify-content: center;
  }
  .front__divider {
    width: 1px;
    height: 220px;
    background: var(--divider);
    flex: none;
  }
  .front__details { padding-left: 34px; color: var(--ink); min-width: 0; }
  .person__name {
    font-size: 28px;
    font-weight: 700;
    letter-spacing: 0.5px;
    text-transform: uppercase;
  }
  .person__title {
    font-size: 22px;
    color: var(--accent);
    margin-top: 2px;
  }
  .contact { list-style: none; margin-top: 26px; }
  .contact__item {
    display: flex;
    align-items: center;
    gap: 10px;
    font-size: 19px;
    line-height: 1.5;
    white-space: nowrap;
  }
  .contact__icon { width: 20px; height: 20px; flex: none; }
  .contact__site-name { color: var(--accent); }
</style>
</head>
<body>
  <section class="card card--back">
    <div class="brand"><span class="brand__dot"></span>Harbor Trench Co</div>
  </section>

  <section class="card card--front">
    <div class="front__brand-area">
      <div class="brand"><span class="brand__dot"></span>Harbor Trench Co</div>
    </div>
    <div class="front__divider"></div>
    <div class="front__details">
      <h1 class="person__name">Marcus Hale</h1>
      <p class="person__title">Managing Director</p>
      <ul class="contact">
        <li class="contact__item">
          <svg class="contact__icon" viewBox="0 0 24 24" aria-hidden="true"><path d="M6.6 10.8a15 15 0 0 0 6.6 6.6l2.2-2.2a1 1 0 0 1 1-.25 11.4 11.4 0 0 0 3.6.57 1 1 0 0 1 1 1V20a1 1 0 0 1-1 1A17 17 0 0 1 3 4a1 1 0 0 1 1-1h3.5a1 1 0 0 1 1 1c0 1.25.2 2.45.57 3.57a1 1 0 0 1-.25 1z" fill="#1a1a1a"/></svg>
          055-987 654 321
        </li>
        <li class="contact__item">
          <svg class="contact__icon" viewBox="0 0 24 24" aria-hidden="true"><rect x="2" y="5" width="20" height="14" fill="#1a1a1a"/><path d="M2 5l10 8 10-8" stroke="#fff" stroke-width="1.6" fill="none"/></svg>
          hello@harbortrenchco.example
        </li>
        <li class="contact__item">
          <svg class="contact__icon" viewBox="0 0 24 24" aria-hidden="true"><g fill="none" stroke="#1a1a1a" stroke-width="1.8"><circle cx="12" cy="12" r="9.5"/><ellipse cx="12" cy="12" rx="4" ry="9.5"/><path d="M2.5 12h19M4 7h16M4 17h16"/></g></svg>
          <span>www.<span class="contact__site-name">harbortrenchco</span>.example</span>
        </li>
      </ul>
    </div>
  </section>
</body>
</html>
```